Ethiopian Restaurant Web Design

San Diego, CA's oldest Ethiopian Restaurant, is redesigning its website. We need to get some designs that embrace the culture and flavors of Ethiopia. They are often featured in local magazines and news stories and we need their site to shine.

Number of Pages Required

3 page

Other font styles liked:
• http://www.amberhollowcafeoc.com

```html
<!DOCTYPE html>
<html lang="en">
<head>
<meta charset="utf-8">
<title>Tana Table Ethiopian Restaurant</title>
<link href="https://fonts.googleapis.com/css2?family=Great+Vibes&family=Playfair+Display:wght@400;600;700&family=Lora:wght@400;600&display=swap" rel="stylesheet">
<style>
:root{
  --red:#d9141b;
  --maroon:#6b0a10;
  --footer:#7a0b11;
  --yellow:#f7dc14;
  --dark:#151515;
  --blush:#f6eced;
  --ink:#1d1d1d;
  --grey:#6e6e6e;
  --green:#1f8f3a;
  --serif:'Playfair Display', Georgia, serif;
  --body:'Lora', Georgia, serif;
  --script:'Great Vibes', cursive;
}
*{margin:0;padding:0;box-sizing:border-box}
html,body{width:1200px;height:4240px;overflow:hidden}
body{font-family:var(--body);color:var(--ink);background:#fff;position:relative}
.abs{position:absolute}
.script{font-family:var(--script);font-weight:400}
.brush{background:var(--yellow);border-radius:40% 10% 40% 10%/60% 20% 60% 20%;font-family:var(--script);color:var(--maroon);display:flex;align-items:center;justify-content:center}

/* hero */
.hero{position:absolute;left:0;top:0;width:1200px;height:660px;overflow:hidden}
.hero-photo{position:absolute;inset:0;background:linear-gradient(120deg,#2a2a26 0%,#1b1c1a 45%,#262520 100%)}
.topbar{position:absolute;left:0;top:0;width:1200px;height:66px;background:var(--red)}
.logo{position:absolute;left:181px;top:0;width:194px;height:99px;background:#f4ecd0;border:3px solid var(--green);display:flex;align-items:center;justify-content:center;font-family:var(--serif);font-weight:700;font-size:34px;color:var(--red)}
.social{position:absolute;top:17px;display:flex;gap:14px;left:679px}
.social span{width:30px;height:30px;border-radius:50%;background:var(--yellow);display:block}
.book-top{left:884px;top:12px;width:135px;height:40px;font-size:22px}
.nav{position:absolute;top:84px;left:469px;display:flex;gap:26px;font-family:var(--serif);font-size:13px;color:#fff}
.hero-text{position:absolute;left:186px;top:204px;color:#fff}
.hero-text .welcome{color:var(--yellow);font-size:30px}
.hero-text .taste{font-size:62px;line-height:1;margin-top:14px}
.hero-text h1{font-family:var(--serif);font-weight:700;font-size:60px;line-height:66px;margin-top:6px}
.hero-text h1 em{font-style:normal;color:var(--yellow)}
.hero-text p{font-size:12.5px;line-height:21px;margin-top:20px;width:420px}
.book-hero{left:186px;top:540px;width:137px;height:42px;font-size:22px}
.dish-brush{left:690px;top:380px;width:430px;height:110px;background:var(--yellow);border-radius:50% 20% 40% 30%}
.dish{left:658px;top:208px;width:400px;height:300px;border-radius:50%;background:radial-gradient(circle at 50% 45%,#4a3424 0%,#6b513c 35%,#d6c6a8 62%,#f5f3ee 75%)}
.price-tag{left:658px;top:474px;width:184px;height:80px;background:var(--red);border-radius:30% 12% 30% 12%;color:#fff;text-align:center;padding-top:10px}
.price-tag b{font-family:var(--serif);font-size:26px;font-weight:700;display:block}
.price-tag i{font-family:var(--script);font-style:normal;color:var(--yellow);font-size:18px}
.dots{left:856px;top:572px;display:flex;gap:10px}
.dots span{width:9px;height:9px;border-radius:50%;background:#a7953a}
.dots span.on{background:var(--yellow);outline:2px solid var(--yellow);outline-offset:2px}

/* services */
.section-title{font-family:var(--serif);font-weight:600;font-size:66px;text-align:center;color:var(--ink)}
.section-title .script{font-size:66px;margin-right:12px}
.section-title .accent{color:var(--yellow)}
.services .section-title{position:absolute;left:0;width:1200px;top:720px}
.services .lead{position:absolute;left:0;width:1200px;top:814px;text-align:center;font-size:13px;color:var(--grey)}
.service{position:absolute;width:260px;text-align:center}
.service .icon{width:70px;height:62px;margin:0 auto;position:relative}
.service .icon:before{content:"";position:absolute;left:0;top:0;width:60px;height:50px;background:#fbe1e3;border-radius:50% 40% 60% 30%}
.service .icon i{position:absolute;left:24px;top:18px;width:28px;height:34px;background:var(--red);border-radius:6px}
.service h3{font-family:var(--serif);font-weight:400;font-size:19px;margin-top:10px}
.service p{font-size:13px;line-height:20.5px;color:var(--grey);margin-top:12px}
.service a{display:block;font-family:var(--script);color:var(--red);font-size:21px;margin-top:18px;text-decoration:none}

/* gursha */
.gursha{position:absolute;left:0;top:1482px;width:1200px;height:658px;background:var(--maroon)}
.frame{position:absolute;border:2px solid #c99a3a;border-radius:30px}
.gursha-photo{left:82px;top:115px;width:436px;height:447px;border-radius:26px;background:radial-gradient(circle at 50% 45%,#6b4a2e 0%,#8a6a48 40%,#3b2a22 75%,#1e1814 100%)}
.gursha-tag{left:272px;top:436px;width:263px;height:156px;background:var(--red);border-radius:36% 18% 30% 22%;color:#fff;padding:26px 0 0 48px}
.gursha-tag b{font-family:var(--serif);font-size:27px;font-weight:700}
.gursha-tag i{font-family:var(--script);font-style:normal;color:var(--yellow);font-size:18px;margin-left:12px}
.gursha-tag p{font-size:10.5px;margin-top:14px;line-height:20px;text-align:right;padding-right:34px}
.gursha-text{left:612px;top:80px;width:400px;color:#fff}
.gursha-text .what{font-size:66px;line-height:1}
.gursha-text h2{font-family:var(--serif);font-weight:700;font-size:62px;line-height:1;margin-top:4px}
.gursha-text h2 em{font-style:normal;color:var(--yellow)}
.gursha-text p{font-size:13px;line-height:20.5px;margin-top:20px}
.kinds{display:flex;gap:24px;margin-top:20px;font-size:34px}
.kinds .first{color:var(--yellow)}
.read-more{width:138px;height:42px;font-size:22px;margin-top:28px}
.call{font-size:13px;margin-top:24px}
.phone{display:flex;align-items:center;gap:10px;color:var(--yellow);font-family:var(--script);font-size:26px;margin-top:6px}

/* menu */
.menu{position:absolute;left:0;top:2140px;width:1200px;height:976px;background:var(--blush)}
.menu .section-title{position:absolute;left:0;width:1200px;top:68px}
.menu .section-title .dark{color:var(--ink)}
.card{position:absolute;width:262px;height:353px;background:#fff;border-radius:12px;overflow:hidden}
.card .shot{height:160px;clip-path:polygon(0 0,100% 0,100% 55%,88% 100%,60% 80%,20% 90%,0 70%)}
.card .count{position:absolute;left:22px;top:148px;font-size:11px;color:var(--red)}
.card h3{position:absolute;left:22px;top:178px;font-family:var(--serif);font-weight:600;font-size:19px}
.card ul{position:absolute;left:22px;right:22px;top:220px;list-style:none;font-size:12px;color:var(--grey)}
.card li{display:flex;justify-content:space-between;line-height:22.5px}
.card a{position:absolute;left:22px;top:300px;font-family:var(--script);color:var(--red);font-size:21px;text-decoration:none}

/* gallery */
.gallery-title{position:absolute;left:183px;top:3184px}
.gallery-title .script{font-size:66px;display:block;line-height:1}
.gallery-title h2{font-family:var(--serif);font-weight:700;font-size:62px;color:var(--yellow);line-height:1;margin-top:-4px}
.view-all{left:818px;top:3238px;width:133px;height:40px;font-size:22px}
.tile{position:absolute;border-radius:14px}

/* footer */
.band{position:absolute;left:0;top:3770px;width:1200px;height:32px;background:linear-gradient(var(--green) 0 6px,var(--yellow) 6px 10px,var(--red) 10px 22px,var(--yellow) 22px 26px,var(--green) 26px 32px)}
.footer{position:absolute;left:0;top:3802px;width:1200px;height:438px;background:var(--footer);color:#fff}
.footer h4{font-family:var(--body);font-weight:400;font-size:16px}
.keep{position:absolute;left:0;width:1200px;top:48px;text-align:center;font-size:16px}
.f-logo{left:181px;top:91px;width:87px;height:41px;background:#f4ecd0;border:2px solid var(--green);color:var(--red);font-family:var(--serif);font-weight:700;font-size:15px;display:flex;align-items:center;justify-content:center}
.subscribe{left:398px;top:91px;width:404px;height:38px;border-radius:19px;background:#5a070b;border:1px solid #9b1a20;font-size:12px;color:#e7cfcf;padding:11px 22px}
.subscribe span{position:absolute;right:6px;top:5px;width:50px;height:26px;border-radius:13px;background:var(--red);display:flex;align-items:center;justify-content:center}
.f-about{left:181px;top:158px;width:200px;font-size:12px;line-height:20px}
.f-social{left:181px;top:280px;display:flex;gap:20px}
.f-social span{width:16px;height:16px;background:#fff;border-radius:50%}
.f-social span:first-child{background:var(--yellow)}
.links{left:431px;top:180px;font-size:12px}
.links ul{list-style:none;margin-top:22px}
.links li{line-height:30px}
.contact{left:640px;top:180px;font-size:12px;width:190px}
.contact .row{display:flex;gap:12px;margin-top:14px;line-height:18px}
.contact svg{flex:none;margin-top:2px}
.hours{left:873px;top:98px;font-size:11.5px}
.hours table{border-collapse:collapse}
.hours th{font-family:var(--body);font-weight:600;font-size:14px;text-align:left;padding-bottom:8px}
.hours td{height:30px;padding-right:28px}
.legal{position:absolute;top:398px;font-size:11px;color:#e9d3d3}
</style>
</head>
<body>

<header class="hero">
  <div class="hero-photo" role="img" aria-label="Dim restaurant dining room interior"></div>
  <div class="topbar"></div>
  <div class="logo">Tana Table</div>
  <div class="social" aria-label="Social links"><span></span><span></span><span></span><span></span></div>
  <div class="abs brush book-top">Book Now</div>
  <nav class="nav"><span>About Us</span><span>Ethiopian Coffee</span><span>Services</span><span>What is Gursha?</span><span>Menu</span><span>Gallery</span><span>Hours</span></nav>
  <div class="hero-text">
    <div class="script welcome">Welcome To Tana Table</div>
    <div class="script taste">Taste the</div>
    <h1>Best <em>Ethiopian</em><br>Food Here</h1>
    <p>A healthy modern protein kitchen featuring a raw juice bar and smoothie bowls and more anytime for you in Ethiopian Restaurant.</p>
  </div>
  <div class="abs brush book-hero">Book Now</div>
  <div class="abs dish-brush"></div>
  <div class="abs dish" role="img" aria-label="Plate of injera topped with beef tibs and greens"></div>
  <div class="abs price-tag"><b>$10.20</b><i>Buy Now</i></div>
  <div class="abs dots"><span></span><span></span><span class="on"></span><span></span><span></span></div>
</header>

<section class="services">
  <h2 class="section-title"><span class="script">Our</span><span class="accent">Services</span></h2>
  <p class="lead">Lorem ipsum dolor sit amet, consectetur adipiscing elit, sed do eiusmod tempor incididunt ut</p>
  <div class="service" style="left:183px;top:880px"><div class="icon"><i></i></div><h3>Corporate Meetings</h3><p>Lorem ipsum dolor sit amet, consectetur adipiscing elit, sed do eiusmod tempor incididunt ut labore et dolore magna aliqua. Quis ipsum suspendisse</p><a>Know More</a></div>
  <div class="service" style="left:469px;top:880px"><div class="icon"><i></i></div><h3>Small Weddings</h3><p>Lorem ipsum dolor sit amet, consectetur adipiscing elit, sed do eiusmod tempor incididunt ut labore et dolore magna aliqua. Quis ipsum suspendisse</p><a>Know More</a></div>
  <div class="service" style="left:754px;top:880px"><div class="icon"><i></i></div><h3>Engagement Parties</h3><p>Lorem ipsum dolor sit amet, consectetur adipiscing elit, sed do eiusmod tempor incididunt ut labore et dolore magna aliqua. Quis ipsum suspendisse</p><a>Know More</a></div>
  <div class="service" style="left:183px;top:1166px"><div class="icon"><i></i></div><h3>Baby Showers</h3><p>Lorem ipsum dolor sit amet, consectetur adipiscing elit, sed do eiusmod tempor incididunt ut labore et dolore magna aliqua. Quis ipsum suspendisse</p><a>Know More</a></div>
  <div class="service" style="left:469px;top:1166px"><div class="icon"><i></i></div><h3>Receptions</h3><p>Lorem ipsum dolor sit amet, consectetur adipiscing elit, sed do eiusmod tempor incididunt ut labore et dolore magna aliqua. Quis ipsum suspendisse</p><a>Know More</a></div>
  <div class="service" style="left:744px;top:1166px;width:280px"><div class="icon"><i></i></div><h3>Community Sponsored Parties</h3><p style="padding:0 10px">Lorem ipsum dolor sit amet, consectetur adipiscing elit, sed do eiusmod tempor incididunt ut labore et dolore magna aliqua. Quis ipsum suspendisse</p><a>Know More</a></div>
</section>

<section class="gursha">
  <div class="frame" style="left:64px;top:98px;width:470px;height:480px;border-right-color:transparent;border-top-color:transparent"></div>
  <div class="frame" style="left:400px;top:100px;width:132px;height:200px;border-left-color:transparent;border-bottom-color:transparent"></div>
  <div class="abs gursha-photo" role="img" aria-label="Hands sharing food from a large platter of injera"></div>
  <div class="abs gursha-tag"><b>$20.00</b><i>Buy Now</i>
    <p>1820 Cedar Grove Avenue Linden Falls,<br>OR 97999</p></div>
  <div class="abs gursha-text">
    <div class="script what">What</div>
    <h2>is <em>Gursha?</em></h2>
    <p>The Ethiopia custom of giving gursha plays up the erotic component of eating. Gursha means mouthful and refers to a morsel of food, which one places carefully in another's mouth, usually as a gesture of affection. Gursha is exchanged between husband and wife, as well as among relatives and friends.</p>
    <div class="kinds script"><span class="first">Injera</span><span>Teff</span><span>Wet</span></div>
    <p style="margin-top:16px">Spongy, flat, unleavened bread, usually prepared from teff, weat or barley and millet.</p>
    <div class="brush read-more">Read More</div>
    <div class="call">For information or to make reservation please call at</div>
    <div class="phone"><svg width="18" height="18" viewBox="0 0 24 24"><path fill="#f7dc14" d="M6.6 10.8c1.4 2.8 3.8 5.1 6.6 6.6l2.2-2.2c.3-.3.7-.4 1-.2 1.1.4 2.3.6 3.6.6.6 0 1 .4 1 1V20c0 .6-.4 1-1 1C10.6 21 3 13.4 3 4c0-.6.4-1 1-1h3.5c.6 0 1 .4 1 1 0 1.3.2 2.5.6 3.6.1.3 0 .7-.2 1z"/></svg>555 010-4821</div>
  </div>
</section>

<section class="menu">
  <h2 class="section-title"><span class="script">Our</span><span class="accent">Food</span> <span class="dark">Menu</span></h2>
  <div class="card" style="left:176px;top:174px"><div class="shot" role="img" aria-label="Fresh green salad" style="background:linear-gradient(135deg,#7fb043,#3f7a2a 60%,#c9483a)"></div><span class="count">59 Item</span><h3>Appetizers</h3><ul><li><span>Green salad</span><span>$7.99</span></li><li><span>Timatim Salad</span><span>$7.99</span></li><li><span>Sambussa</span><span>$2.50</span></li></ul><a>Know More</a></div>
  <div class="card" style="left:469px;top:174px"><div class="shot" role="img" aria-label="Grilled fish with onions" style="background:linear-gradient(135deg,#5a4030,#8a7060 50%,#b84a5a)"></div><span class="count">59 Item</span><h3>Entrees</h3><ul><li><span>Green salad</span><span>$7.99</span></li><li><span>Timatim Salad</span><span>$7.99</span></li><li><span>Sambussa</span><span>$2.50</span></li></ul><a>Know More</a></div>
  <div class="card" style="left:754px;top:174px"><div class="shot" role="img" aria-label="Coffee poured into a glass" style="background:linear-gradient(135deg,#1a1a1a,#3a2418 60%,#6a4a38)"></div><span class="count">59 Item</span><h3>Coffee</h3><ul><li><span>Green salad</span><span>$7.99</span></li><li><span>Timatim Salad</span><span>$7.99</span></li><li><span>Sambussa</span><span>$2.50</span></li></ul><a>Know More</a></div>
  <div class="card" style="left:176px;top:550px"><div class="shot" role="img" aria-label="Vegetable salad in a bowl" style="background:linear-gradient(135deg,#b89a70,#5e8a3a 50%,#c8443a)"></div><span class="count">59 Item</span><h3>Vegetarian Entrees</h3><ul><li><span>Green salad</span><span>$7.99</span></li><li><span>Timatim Salad</span><span>$7.99</span></li><li><span>Sambussa</span><span>$2.50</span></li></ul><a>Know More</a></div>
  <div class="card" style="left:469px;top:550px"><div class="shot" role="img" aria-label="Glazed grilled meat" style="background:linear-gradient(135deg,#d8d0c0,#4a2c1c 55%,#2a1810)"></div><span class="count">59 Item</span><h3>House Specialities</h3><ul><li><span>Green salad</span><span>$7.99</span></li><li><span>Timatim Salad</span><span>$7.99</span></li><li><span>Sambussa</span><span>$2.50</span></li></ul><a>Know More</a></div>
  <div class="card" style="left:754px;top:550px"><div class="shot" role="img" aria-label="Colourful cocktails" style="background:linear-gradient(135deg,#2a2a2a,#d8a040 40%,#c8303a 70%,#3a7ab8)"></div><span class="count">59 Item</span><h3>Beverages</h3><ul><li><span>Green salad</span><span>$7.99</span></li><li><span>Timatim Salad</span><span>$7.99</span></li><li><span>Sambussa</span><span>$2.50</span></li></ul><a>Know More</a></div>
</section>

<section class="gallery">
  <div class="gallery-title"><span class="script">Our</span><h2>Gallery</h2></div>
  <div class="abs brush view-all">View All</div>
  <div class="tile" style="left:183px;top:3386px;width:263px;height:314px;background:linear-gradient(160deg,#cfc6b8,#4a2c1c 50%,#2a1810)" role="img" aria-label="Glazed grilled meat"></div>
  <div class="tile" style="left:469px;top:3190px;width:262px;height:300px;background:linear-gradient(135deg,#2a2a2a,#d8a040 35%,#c8303a 65%,#9ac060)" role="img" aria-label="Cocktails on a bar"></div>
  <div class="tile" style="left:469px;top:3514px;width:262px;height:186px;background:linear-gradient(135deg,#5a4030,#8a7060 50%,#b84a5a)" role="img" aria-label="Grilled fish with onions"></div>
  <div class="tile" style="left:754px;top:3341px;width:262px;height:359px;background:radial-gradient(circle at 50% 40%,#4a3424,#7a6048 40%,#e0d6c4 70%,#f4f1ea)" role="img" aria-label="Injera with beef tibs and greens"></div>
</section>

<div class="band"></div>
<footer class="footer">
  <div class="keep">KEEP UP-TO-DATE WITH US</div>
  <div class="abs f-logo">Tana Table</div>
  <div class="abs subscribe">Email address<span><svg width="14" height="14" viewBox="0 0 24 24"><path fill="#f7dc14" d="M2 21l21-9L2 3v7l15 2-15 2z"/></svg></span></div>
  <p class="abs f-about">Lorem ipsum dolor sit amet, consectetur adipiscing elit, sed do eiusmod tempor incididunt ut labore et dolore magna aliqua.</p>
  <div class="abs f-social" aria-label="Social links"><span></span><span></span><span></span><span></span></div>
  <div class="abs links"><h4>Quick Links</h4><ul><li>About Us</li><li>Services</li><li>What is Gursha?</li><li>Menu</li><li>Gallery</li></ul></div>
  <div class="abs contact"><h4>Contact</h4>
    <div class="row" style="margin-top:26px"><svg width="12" height="16" viewBox="0 0 12 16"><path fill="#f7dc14" d="M6 0a6 6 0 0 0-6 6c0 4.5 6 10 6 10s6-5.5 6-10a6 6 0 0 0-6-6zm0 8.5A2.5 2.5 0 1 1 6 3.5a2.5 2.5 0 0 1 0 5z"/></svg><span>1820 Cedar Grove Avenue Linden Falls,OR 97999</span></div>
    <div class="row"><svg width="16" height="12" viewBox="0 0 16 12"><rect width="16" height="12" rx="1" fill="#f7dc14"/><path d="M1 1l7 6 7-6" stroke="#7a0b11" fill="none" stroke-width="1.4"/></svg><span>info@tanatable.com</span></div>
    <div class="row"><svg width="14" height="14" viewBox="0 0 24 24"><path fill="#f7dc14" d="M6.6 10.8c1.4 2.8 3.8 5.1 6.6 6.6l2.2-2.2c.3-.3.7-.4 1-.2 1.1.4 2.3.6 3.6.6.6 0 1 .4 1 1V20c0 .6-.4 1-1 1C10.6 21 3 13.4 3 4c0-.6.4-1 1-1h3.5c.6 0 1 .4 1 1 0 1.3.2 2.5.6 3.6.1.3 0 .7-.2 1z"/></svg><span>555 010-4821</span></div>
  </div>
  <div class="abs hours"><table>
    <tr><th>Day</th><th>Hours</th></tr>
    <tr><td>Sunday</td><td>12–10PM</td></tr>
    <tr><td>Monday</td><td>CLOSED</td></tr>
    <tr><td>Tuesday</td><td>12–10PM</td></tr>
    <tr><td>Wednesday</td><td>12–10PM</td></tr>
    <tr><td>Thursday</td><td>12–10PM</td></tr>
    <tr><td>Friday</td><td>12–10PM</td></tr>
    <tr><td>Saturday</td><td>12–10PM</td></tr>
  </table></div>
  <div class="legal" style="left:183px">copyright @ 2022 Tana Table. All right reserved.</div>
  <div class="legal" style="left:872px">Privacy Policy | Site Map</div>
</footer>

</body>
</html>
```